TRIVAN 2026 Flyer for Conference

TRIVAN needs a design for a 1-page flyer that we will hand out at an upcoming event & then later post online as a pdf. There are 3 elements which need to be on the flyer:

1) A logo. This should be prominent on the design (e.g., in the middle). The flyer should use the colors that are in that logo (e.g., for accents, design elements, and/or text; not all of these have to be used):
Dark blue: #185577
Med blue: #327C9A
Teal: #4EB1C2
Light Teal: #9EDBE6

2) The conference theme -- Forests of Wonder: Climbing toward Research Fluency -- should be at the flyer's top.

3) Finally, these six tracks should be listed below the theme and the logo (it's font size should be at least a couple sizes smaller than the size used for the theme):
- Pearls of Pedagogy: Teaching Techniques that Work
- The Depth Gauge: Measuring Instructional Impact
- Techtonic Shifts: Innovation and Educational Technology
- Captain's Log: Navigating Leadership in Library Instruction
- Swimming Together: Collaborating with Others
- The Bermuda Triangle: Exploring (Seemingly) Eternal Challenges

Font styles to use
Sans Serif

Colors
0094D4
00A9DD
6FCCEA
C7EBF8
E9F6FB

Requirements
Must have
• The 3 elements listed in the description: 1) the logo, 2) the text of the theme and 3) the text for the tracks.

```html
<!DOCTYPE html>
<html lang="en">
<head>
<meta charset="utf-8">
<title>TRIVAN 2026 Conference Flyer</title>
<link href="https://fonts.googleapis.com/css2?family=Poppins:wght@400;500;600;700;800&display=swap" rel="stylesheet">
<style>
  :root {
    --stage: #a3a3a3;
    --paper: #ffffff;
    --navy: #0b3b62;
    --dark-blue: #185577;
    --med-blue: #327c9a;
    --teal: #4eb1c2;
    --light-teal: #9edbe6;
    --cyan: #4fd0ec;
    --ink: #1a1a1a;
    --white: #ffffff;
  }
  * { margin: 0; padding: 0; box-sizing: border-box; }
  html, body { width: 1200px; height: 1200px; overflow: hidden; }
  body {
    background: var(--stage);
    font-family: "Poppins", sans-serif;
    position: relative;
  }
  .flyer {
    position: absolute;
    left: 188px; top: 68px;
    width: 825px; height: 1068px;
    background: var(--paper);
    overflow: hidden;
  }
  .brand {
    position: absolute;
    left: 0; right: 0; top: 82px;
    display: flex; align-items: center; justify-content: center; gap: 14px;
  }
  .brand-dot {
    width: 46px; height: 46px; border-radius: 50%;
    background: var(--teal);
  }
  .brand-name {
    font-weight: 700; font-size: 52px; line-height: 1;
    color: var(--dark-blue); letter-spacing: 1px;
  }
  .sky-photo {
    position: absolute; left: 0; top: 199px; width: 825px; height: 733px;
    background: linear-gradient(180deg, #ffffff 0%, #f2f6f9 12%, #dbe6ee 40%, #c9d8e4 70%, #b8c9d6 100%);
  }
  .theme {
    position: absolute; left: 0; right: 0; top: 206px; text-align: center;
  }
  .theme-title {
    font-weight: 700; font-size: 55px; line-height: 1.1;
    color: var(--med-blue); letter-spacing: 0.5px;
  }
  .theme-sub {
    font-weight: 600; font-size: 33px; line-height: 1.2;
    color: var(--ink); margin-top: 2px;
  }
  .tracks-panel {
    position: absolute; left: 61px; top: 322px; width: 702px; height: 300px;
    background: linear-gradient(180deg, #0c3d63 0%, #0f4168 60%, #1b4d72 100%);
    border-radius: 26px 26px 0 0;
  }
  .tracks {
    position: absolute; left: 0; top: 0; width: 100%; height: 100%;
  }
  .track {
    position: absolute; display: flex; gap: 8px; width: 215px;
  }
  .track-icon {
    flex: 0 0 31px; width: 31px; height: 31px; border-radius: 50%;
    background: var(--cyan); border: 2px solid var(--white);
    display: flex; align-items: center; justify-content: center; margin-top: 2px;
  }
  .track-icon svg { width: 18px; height: 18px; }
  .track-title {
    font-weight: 700; font-size: 17px; line-height: 18.5px;
    color: var(--cyan); text-transform: uppercase;
  }
  .track-desc {
    font-weight: 500; font-size: 13.5px; line-height: 16px;
    color: var(--white); margin-top: 5px;
  }
  .track-desc.tight { margin-top: 1px; }
  .city-photo {
    position: absolute; left: 0; top: 588px; width: 825px; height: 344px;
    background: linear-gradient(180deg, #6f86a8 0%, #c7b79a 25%, #e6d7bf 50%, #d98a5c 72%, #eae6df 100%);
  }
  .footer {
    position: absolute; left: 0; top: 943px; width: 825px; height: 125px;
    background: var(--navy);
    display: flex; align-items: center; justify-content: center;
  }
  .url {
    font-weight: 400; font-size: 38px; letter-spacing: 3.2px; color: var(--white);
  }
  .url .domain { color: var(--cyan); }
</style>
</head>
<body>
  <main class="flyer">
    <div class="sky-photo" role="img" aria-label="Photo backdrop of a bright sky with soft clouds"></div>

    <div class="brand">
      <span class="brand-dot"></span>
      <span class="brand-name">TRIVAN 2026</span>
    </div>

    <header class="theme">
      <h1 class="theme-title">FORESTS OF WONDER</h1>
      <p class="theme-sub">Climbing toward Research Fluency</p>
    </header>

    <section class="tracks-panel">
      <div class="tracks">
        <div class="track" style="left:22px; top:49px;">
          <span class="track-icon"><svg viewBox="0 0 18 18" fill="none" stroke="#0b3b62" stroke-width="1.3"><rect x="6" y="3" width="10" height="7"/><circle cx="4" cy="9" r="1.6"/><path d="M1.5 15c0-2 1-3.5 2.5-3.5S6.5 13 6.5 15"/></svg></span>
          <div><h2 class="track-title">Pearls of<br>Pedagogy</h2><p class="track-desc">Teaching Techniques<br>that Work</p></div>
        </div>
        <div class="track" style="left:249px; top:49px;">
          <span class="track-icon"><svg viewBox="0 0 18 18" fill="none" stroke="#0b3b62" stroke-width="1.3"><circle cx="9" cy="9" r="3"/><path d="M9 2v2.5M9 13.5V16M2 9h2.5M13.5 9H16M4 4l1.8 1.8M12.2 12.2L14 14M4 14l1.8-1.8M12.2 5.8L14 4"/></svg></span>
          <div><h2 class="track-title">Techtonic<br>Shifts</h2><p class="track-desc">Innovation and<br>Educational Technology</p></div>
        </div>
        <div class="track" style="left:475px; top:49px;">
          <span class="track-icon"><svg viewBox="0 0 18 18" fill="none" stroke="#0b3b62" stroke-width="1.3"><circle cx="12" cy="6" r="1.6"/><path d="M3 9l5-2 2 3M1.5 12.5c1.5 1 3 1 4.5 0s3-1 4.5 0 3 1 4.5 0M1.5 15.5c1.5 1 3 1 4.5 0s3-1 4.5 0 3 1 4.5 0"/></svg></span>
          <div><h2 class="track-title">Swimming<br>Together</h2><p class="track-desc">Collaborating with<br>Others</p></div>
        </div>
        <div class="track" style="left:22px; top:144px; width:225px;">
          <span class="track-icon"><svg viewBox="0 0 18 18" fill="none" stroke="#0b3b62" stroke-width="1.3"><path d="M2 13a7 7 0 0 1 14 0"/><path d="M9 13l3-4"/><circle cx="9" cy="13" r="1"/></svg></span>
          <div><h2 class="track-title">The Depth Gauge</h2><p class="track-desc tight">Measuring<br>Instructional Impact</p></div>
        </div>
        <div class="track" style="left:249px; top:143px;">
          <span class="track-icon"><svg viewBox="0 0 18 18" fill="none" stroke="#0b3b62" stroke-width="1.3"><path d="M5 5h8l-1 2H6z"/><circle cx="9" cy="9.5" r="2.3"/><path d="M4 16c0-3 2-4.5 5-4.5s5 1.5 5 4.5"/></svg></span>
          <div><h2 class="track-title">Captain's Log</h2><p class="track-desc">Navigating Leadership<br>in Library Instruction</p></div>
        </div>
        <div class="track" style="left:475px; top:144px; width:225px;">
          <span class="track-icon"><svg viewBox="0 0 18 18" fill="none" stroke="#0b3b62" stroke-width="1.3"><path d="M9 3l6.5 12h-13z"/><path d="M9 8v3.5M9 13v.5"/></svg></span>
          <div><h2 class="track-title">The Bermuda<br>Triangle</h2><p class="track-desc">Exploring (Seemingly)<br>Eternal Challenges</p></div>
        </div>
      </div>
    </section>

    <div class="city-photo" role="img" aria-label="Aerial photo of the host city skyline with historic towers, tiled roofs, palm trees and mountains"></div>

    <footer class="footer">
      <p class="url">www.<span class="domain">trivanconference</span>.org</p>
    </footer>
  </main>
</body>
</html>
```